New innovative Food Supplements for Women’s Health needs label design

We are launching a line of food supplements designed specifically for women’s health, and we need a standout label design that appeals to health-conscious women and communicates high quality, premium and trust.

Industry/Entity Type

Consumer products, pharmacy, online

Requirements
Must have
• One label design for one product - see details in brief

```html
<!DOCTYPE html>
<html lang="en">
<head>
<meta charset="utf-8">
<title>Seraline Supreme Label</title>
<link rel="stylesheet" href="https://fonts.googleapis.com/css2?family=Montserrat:wght@400;700&family=Questrial&display=swap">
<style>
  :root {
    --ink: #111111;
    --paper: #ffffff;
    --trim: #e01e2b;
  }
  html, body {
    margin: 0;
    padding: 0;
    width: 1200px;
    height: 576px;
    overflow: hidden;
    background: var(--paper);
  }
  .sheet {
    display: block;
    width: 1200px;
    height: 576px;
  }
  .dimension-label {
    font-family: "Montserrat", sans-serif;
    font-weight: 700;
    font-size: 17px;
    fill: var(--ink);
  }
  .dimension-line { stroke: var(--ink); stroke-width: 1.5; }
  .trim-line { fill: none; stroke: var(--trim); stroke-width: 1.5; }
  .spine { fill: var(--ink); }
  .brand-name {
    font-family: "Questrial", sans-serif;
    font-weight: 400;
    font-size: 31px;
    letter-spacing: 12px;
    fill: var(--ink);
  }
  .product-name {
    font-family: "Questrial", sans-serif;
    font-size: 26px;
    fill: var(--ink);
  }
  .tagline-band { fill: var(--ink); }
  .tagline {
    font-family: "Montserrat", sans-serif;
    font-weight: 700;
    font-size: 12.6px;
    fill: var(--paper);
  }
  .bullet-mark { fill: var(--ink); }
  .benefit {
    font-family: "Montserrat", sans-serif;
    font-weight: 700;
    font-size: 9.9px;
    fill: var(--ink);
  }
  .volume {
    font-family: "Montserrat", sans-serif;
    font-weight: 700;
    font-size: 11px;
    fill: var(--ink);
  }
  .seal-ring { fill: none; stroke: var(--ink); stroke-width: 1.5; }
</style>
</head>
<body>
<svg class="sheet" viewBox="0 0 1200 576" xmlns="http://www.w3.org/2000/svg">
  <!-- width dimension -->
  <text class="dimension-label" x="622" y="133" text-anchor="middle">235mm</text>
  <line class="dimension-line" x1="155" y1="142" x2="1068" y2="142"/>

  <!-- height dimension -->
  <line class="dimension-line" x1="135" y1="166" x2="135" y2="461"/>
  <text class="dimension-label" x="126" y="300" text-anchor="middle" transform="rotate(-90 126 300)">77mm</text>

  <!-- label trim -->
  <rect class="trim-line" x="153" y="164.5" width="915" height="297.5"/>

  <!-- front panel spine -->
  <rect class="spine" x="479.5" y="186" width="3.5" height="277"/>

  <!-- brand -->
  <text class="brand-name" x="495" y="219">VELORIA</text>

  <!-- certification seal -->
  <g class="seal" role="img" aria-label="Certification seal">
    <circle class="seal-ring" cx="697" cy="277" r="43"/>
    <circle class="seal-ring" cx="697" cy="277" r="30"/>
  </g>

  <!-- product name -->
  <text class="product-name" x="494" y="317">SERALINE</text>
  <text class="product-name" x="494" y="337">SUPREME</text>

  <!-- tagline -->
  <rect class="tagline-band" x="496" y="346" width="211" height="14"/>
  <text class="tagline" x="500.5" y="358">FOR SKIN, HAIR AND NAILS</text>

  <!-- benefits -->
  <g class="benefits">
    <rect class="bullet-mark" x="494" y="377" width="5" height="5"/>
    <text class="benefit" x="503.5" y="384">HYDROLYZED MARINE COLLAGEN 11000 MG</text>

    <rect class="bullet-mark" x="494" y="389" width="5" height="5"/>
    <text class="benefit" x="503.5" y="396">POWERFUL ANTI-AGEING COMBO: RETINOL +</text>
    <text class="benefit" x="503.5" y="405">HYALURONIC ACID</text>

    <rect class="bullet-mark" x="494" y="410" width="5" height="5"/>
    <text class="benefit" x="503.5" y="417">SUPPORTIVE MULTIVITAMINS: VITAMINS</text>
    <text class="benefit" x="503.5" y="426">SELENIUM, SILICON, MSM</text>
  </g>

  <!-- volume -->
  <text class="volume" x="494" y="446">500 ML</text>
</svg>
</body>
</html>
```